BrightMesa Business Card Contest

We are looking for a modern business card that catches attention and is unique. Attached is the brand guide and logo files. Please note that the back side (not the side with our name and info) with be UV raise printed, so have fun with the design there. We want to include Name, Title, Phone number, email, website.

Contact Information for Business Card

Please see project description

```html
<!DOCTYPE html>
<html lang="en">
<head>
<meta charset="utf-8">
<title>BrightMesa Business Card</title>
<link href="https://fonts.googleapis.com/css2?family=Montserrat:wght@400;500;700&display=swap" rel="stylesheet">
<style>
  :root {
    --backdrop: #cfcecb;
    --card-white: #ffffff;
    --card-dark: #202127;
    --pattern-light: #3a3e4a;
    --pattern-dark: #15161b;
    --ink: #1c1d22;
    --ink-soft: #6f7075;
    --navy: #0d3a8a;
    --blue: #1f6fc9;
    --cyan: #1cb6e3;
    --mist: #b7c7d6;
    --orange: #f08a22;
    --red: #e0301e;
    --accent-text: #3b9ad9;
  }
  * { margin: 0; padding: 0; box-sizing: border-box; }
  html, body { width: 1200px; height: 801px; overflow: hidden; }
  body {
    background: var(--backdrop);
    font-family: "Montserrat", Arial, sans-serif;
    position: relative;
  }
  .card {
    position: absolute;
    top: 246px;
    width: 540px;
    height: 309px;
    border-radius: 3px;
    box-shadow: 0 10px 28px rgba(0,0,0,0.22);
    overflow: hidden;
  }

  /* Back side */
  .card-back { left: 30px; background: var(--card-dark); }
  .raised-pattern {
    position: absolute;
    left: 40px;
    top: 120px;
    width: 230px;
    height: 160px;
    background: linear-gradient(135deg, var(--pattern-light), var(--pattern-dark));
    clip-path: polygon(20% 0, 100% 22%, 92% 100%, 0 100%, 8% 40%);
  }
  .back-wordmark {
    position: absolute;
    right: 40px;
    top: 118px;
    font-size: 40px;
    font-weight: 500;
    color: var(--accent-text);
    letter-spacing: 0.5px;
  }

  /* Front side */
  .card-front { left: 630px; background: var(--card-white); }
  .brand {
    position: absolute;
    left: 34px;
    top: 132px;
    display: flex;
    align-items: center;
    gap: 10px;
  }
  .brand-square { width: 22px; height: 22px; background: var(--blue); }
  .brand-name { font-size: 32px; font-weight: 500; color: var(--ink); }
  .divider {
    position: absolute;
    left: 268px;
    top: 86px;
    width: 2px;
    height: 114px;
    background: linear-gradient(var(--navy), var(--cyan) 45%, var(--orange) 75%, var(--red));
  }
  .details { position: absolute; left: 290px; top: 88px; }
  .person-name { font-size: 17px; font-weight: 700; color: var(--ink); letter-spacing: 0.3px; }
  .person-title { font-size: 14px; color: var(--ink-soft); margin-top: 2px; }
  .contact-list { list-style: none; margin-top: 14px; }
  .contact-list li {
    display: flex;
    align-items: center;
    gap: 8px;
    font-size: 13.5px;
    color: var(--ink-soft);
    line-height: 22px;
  }
  .contact-list svg { width: 13px; height: 13px; flex: none; }
  .color-band {
    position: absolute;
    left: 0; right: 0; bottom: 0;
    height: 9px;
    background: linear-gradient(90deg, var(--navy), var(--blue) 12%, var(--cyan) 35%, var(--mist) 60%, var(--orange) 80%, var(--red));
  }
</style>
</head>
<body>
  <section class="card card-back">
    <div class="raised-pattern" role="img" aria-label="Raised UV-printed angular pattern in dark charcoal tones"></div>
    <div class="back-wordmark">BrightMesa</div>
  </section>

  <section class="card card-front">
    <div class="brand">
      <span class="brand-square"></span>
      <span class="brand-name">BrightMesa</span>
    </div>
    <div class="divider"></div>
    <div class="details">
      <div class="person-name">DANA WHITFIELD</div>
      <div class="person-title">President</div>
      <ul class="contact-list">
        <li>
          <svg viewBox="0 0 16 16"><path fill="#1f6fc9" d="M3.6 1.5l2.3 2.7-1.3 1.7c.9 2 2.5 3.6 4.5 4.5l1.7-1.3 2.7 2.3-1.2 2.4C7 13.5 2.5 9 1.2 2.7z"/></svg>
          014-278-5530
        </li>
        <li>
          <svg viewBox="0 0 16 16"><rect x="1" y="3" width="14" height="10" fill="#f08a22"/><path d="M1 3.5l7 5 7-5" stroke="#fff" stroke-width="1.4" fill="none"/></svg>
          info@brightmesa.com
        </li>
        <li>
          <svg viewBox="0 0 16 16" fill="none" stroke="#e0301e" stroke-width="1.4"><circle cx="8" cy="8" r="6.3"/><ellipse cx="8" cy="8" rx="2.8" ry="6.3"/><path d="M1.7 8h12.6M2.8 4.8h10.4M2.8 11.2h10.4"/></svg>
          www.brightmesa.com
        </li>
      </ul>
    </div>
    <div class="color-band"></div>
  </section>
</body>
</html>
```